Lionel Arbusto and Dwight Halvorsen Advertisement

We would like an ad that conveys understated elegance. We are a company that purchases estate jewelry watches and diamonds. We care to a wealthy, upscale clientele.

Target Market(s)

Wealthy upscale.

Industry/Entity Type

It Company

Requirements
Must have
• Elegant Design. Crisp Clean. Attached a doc of how the ad should be arranged.

```html
<!DOCTYPE html>
<html lang="en">
<head>
<meta charset="utf-8">
<title>Lionel Arbusto &amp; Dwight Halvorsen — Ready To Sell?</title>
<link rel="stylesheet" href="https://fonts.googleapis.com/css2?family=Josefin+Sans:wght@300&family=Roboto:wght@300;400&display=swap">
<style>
  :root {
    --backdrop: #2e2420;
    --paper: #ffffff;
    --ink: #1e1e1e;
    --ink-soft: #3a3a3a;
    --mist-light: #f4f4f4;
    --mist-mid: #dcdcdc;
    --mist-deep: #bdbdbd;
    --stone-light: #ffffff;
    --stone-mid: #d6d6d6;
    --stone-deep: #8e8e8e;
    --band: #2b2b2b;
    --band-text: #f2f2f2;
  }
  html, body {
    margin: 0;
    padding: 0;
    width: 1200px;
    height: 1200px;
    overflow: hidden;
    background: var(--backdrop);
  }
  .ad {
    position: absolute;
    left: 197px;
    top: 28px;
    width: 806px;
    height: 1143px;
    background: linear-gradient(180deg, #ffffff 0%, #f2f2f2 20%, #eaeaea 45%, #f4f4f4 70%, #ffffff 80%);
    overflow: hidden;
    font-family: "Roboto", sans-serif;
    color: var(--ink);
    text-align: center;
  }
  .headline {
    position: absolute;
    top: 100px;
    left: 0;
    width: 100%;
    margin: 0;
    font-family: "Josefin Sans", sans-serif;
    font-weight: 300;
    font-size: 108px;
    line-height: 1;
    letter-spacing: -6px;
    color: var(--ink);
    padding-left: 20px;
    box-sizing: border-box;
  }
  .hero-backdrop {
    position: absolute;
    top: 240px;
    left: 0;
    width: 806px;
    height: 500px;
  }
  .hero-stone {
    position: absolute;
    top: 318px;
    left: 242px;
    width: 345px;
    height: 340px;
  }
  .brand {
    position: absolute;
    top: 828px;
    left: 0;
    width: 100%;
  }
  .brand-name {
    margin: 0;
    font-family: "Roboto", sans-serif;
    font-weight: 300;
    font-size: 18px;
    letter-spacing: 1.2px;
    text-transform: uppercase;
    color: var(--ink-soft);
  }
  .brand-tagline {
    display: flex;
    align-items: center;
    justify-content: center;
    gap: 8px;
    margin-top: 3px;
    font-family: "Roboto", sans-serif;
    font-weight: 300;
    font-size: 10px;
    letter-spacing: 1.5px;
    text-transform: uppercase;
    color: var(--ink-soft);
  }
  .brand-tagline::before,
  .brand-tagline::after {
    content: "";
    width: 110px;
    height: 1px;
    background: var(--ink-soft);
  }
  .service {
    position: absolute;
    top: 892px;
    left: 0;
    width: 100%;
    font-weight: 300;
    font-size: 23px;
    line-height: 37px;
    color: var(--ink-soft);
  }
  .service p { margin: 0; }
  .address {
    position: absolute;
    top: 984px;
    left: 0;
    width: 100%;
    font-style: normal;
    font-weight: 300;
    font-size: 18px;
    line-height: 24px;
    color: var(--ink-soft);
  }
  .contact-band {
    position: absolute;
    top: 1042px;
    left: 0;
    width: 100%;
    height: 57px;
    background: var(--band);
    color: var(--band-text);
    display: flex;
    align-items: center;
    justify-content: center;
    gap: 18px;
    font-weight: 300;
    font-size: 21px;
  }
  .contact-band .divider { opacity: 0.8; }
</style>
</head>
<body>
  <main class="ad">
    <h1 class="headline">Ready To Sell?</h1>

    <svg class="hero-backdrop" viewBox="0 0 806 500" role="img" aria-label="Soft silver waves with faint stars and snowflakes behind the diamond">
      <defs>
        <linearGradient id="waveTone" x1="0" y1="0" x2="0" y2="1">
          <stop offset="0" stop-color="#eeeeee" stop-opacity="0"/>
          <stop offset="0.35" stop-color="#d4d4d4"/>
          <stop offset="0.6" stop-color="#c2c2c2"/>
          <stop offset="1" stop-color="#f2f2f2" stop-opacity="0"/>
        </linearGradient>
        <radialGradient id="floorGlow" cx="0.5" cy="0.5" r="0.5">
          <stop offset="0" stop-color="#ffffff"/>
          <stop offset="1" stop-color="#ffffff" stop-opacity="0"/>
        </radialGradient>
      </defs>
      <rect x="0" y="0" width="806" height="500" fill="url(#waveTone)"/>
      <ellipse cx="403" cy="440" rx="460" ry="120" fill="url(#floorGlow)"/>
    </svg>

    <svg class="hero-stone" viewBox="0 0 345 340" role="img" aria-label="Emerald-cut diamond photograph">
      <defs>
        <linearGradient id="stoneTone" x1="0" y1="0" x2="1" y2="1">
          <stop offset="0" stop-color="var(--stone-light)"/>
          <stop offset="0.5" stop-color="var(--stone-mid)"/>
          <stop offset="1" stop-color="var(--stone-deep)"/>
        </linearGradient>
      </defs>
      <polygon points="75,12 280,2 335,55 340,250 300,322 110,338 25,290 10,70" fill="url(#stoneTone)"/>
    </svg>

    <div class="brand">
      <p class="brand-name">Lionel Arbusto &amp; Dwight Halvorsen</p>
      <div class="brand-tagline">Your Best Option</div>
    </div>

    <div class="service">
      <p>Utmost Discretion</p>
      <p>By Appointment</p>
    </div>

    <address class="address">
      Casa Serena<br>
      118-B Linden Avenue Palm Grove, FL 33401
    </address>

    <div class="contact-band">
      <span class="email">concierge@arbustohalvorsen.com</span>
      <span class="divider">|</span>
      <span class="phone">561.555.0142</span>
    </div>
  </main>
</body>
</html>
```